Need a flyer to leave behind when visiting clients or at shows

Glossy colorful tri-fold flyer with the same information that is on my web site www.brevalinkpro.com. I am open to a little modern or creative take on the typical brochure. I created the web site so I can provide any raw files needed from it. I would also like the ability to edit this flyer in the future in Adobe Photoshop Elements

```html
<!DOCTYPE html>
<html lang="en">
<head>
<meta charset="utf-8">
<title>Brevalink Pro – Tri-fold Brochure</title>
<link href="https://fonts.googleapis.com/css2?family=Montserrat:wght@400;500;600;700&display=swap" rel="stylesheet">
<style>
  :root{
    --bg:#eceef4;
    --purple:#6a35c4;
    --purple-deep:#5a3aa8;
    --violet-wave:#5b4bb0;
    --blue-wave:#3a6fc0;
    --cyan:#00bcd8;
    --cyan-light:#5fd3e6;
    --panel-grey:#f1f1f2;
    --box-grey:#e2e1e3;
    --ink:#1f1f24;
    --white:#ffffff;
  }
  *{margin:0;padding:0;box-sizing:border-box;}
  html,body{width:1200px;height:1200px;overflow:hidden;}
  body{background:var(--bg);font-family:'Montserrat',sans-serif;color:var(--ink);position:relative;}

  .brochure{position:absolute;left:0;top:152px;width:1200px;height:896px;background:var(--panel-grey);overflow:hidden;}
  .waves{position:absolute;inset:0;width:1200px;height:896px;}
  .panel{position:absolute;top:0;height:896px;width:400px;}
  .panel-about{left:0;}
  .panel-values{left:400px;}
  .panel-services{left:800px;}

  /* About panel */
  .about-photo{position:absolute;left:0;top:0;width:400px;height:520px;
    background:linear-gradient(180deg,#dfeef5 0%,#b9dfeb 40%,#5ccde2 80%,var(--cyan) 100%);}
  .about-body{position:absolute;left:35px;top:513px;width:345px;color:var(--white);}
  .about-title{font-size:27px;font-weight:700;color:var(--purple);margin-bottom:14px;}
  .about-sub{font-size:17px;font-weight:600;line-height:1.2;}
  .about-text{font-size:16px;font-weight:400;line-height:1.35;margin-bottom:18px;}

  /* Core values */
  .values-box{position:absolute;left:62px;top:0;width:274px;height:333px;background:var(--box-grey);}
  .section-title{font-size:22px;font-weight:400;color:var(--purple);letter-spacing:.2px;}
  .section-title b{font-weight:700;}
  .values-box .section-title{position:absolute;left:26px;top:36px;}
  .value{position:absolute;width:120px;text-align:center;}
  .value-tile{width:86px;height:70px;margin:0 auto;background:var(--purple);display:flex;align-items:center;justify-content:center;}
  .value-label{margin-top:9px;font-size:10px;color:var(--purple);line-height:1.35;}
  .value-label.big{font-size:15px;margin-top:14px;}

  .objective-title{position:absolute;left:40px;top:390px;}
  .objective{position:absolute;left:70px;display:flex;align-items:center;gap:12px;font-size:15px;line-height:1.35;}
  .objective svg{flex:none;}

  .badge{position:absolute;left:127px;top:697px;width:177px;height:172px;background:#e4e4e6;padding:7px;}
  .badge-inner{width:100%;height:100%;background:var(--white);display:flex;align-items:center;justify-content:center;}

  /* Services */
  .services-title{position:absolute;left:30px;top:28px;}
  .services-text{position:absolute;left:33px;top:60px;width:340px;font-size:15.5px;line-height:1.26;}
  .it-title{position:absolute;left:48px;top:230px;font-size:21px;font-weight:700;color:var(--purple);}
  .it-list{position:absolute;left:26px;top:278px;list-style:none;font-size:15.5px;line-height:20.5px;}
  .it-list li{display:flex;align-items:center;gap:7px;}
  .it-photo{position:absolute;left:-36px;top:435px;width:372px;height:372px;border-radius:50%;
    border:5px solid #f4f4f6;
    background:radial-gradient(circle at 65% 35%,#4f8fd8 0%,#2b5ea8 40%,#182f5e 80%,#101e40 100%);}
</style>
</head>
<body>
<main class="brochure">
  <svg class="waves" viewBox="0 0 1200 896" aria-hidden="true">
    <rect x="0" y="0" width="400" height="896" fill="var(--cyan)"/>
    <path d="M0 780 C120 800 250 830 400 820 L400 896 L0 896 Z" fill="var(--violet-wave)"/>
    <path d="M0 820 C150 850 280 860 400 840 L400 896 L0 896 Z" fill="var(--blue-wave)" opacity=".7"/>
    <path d="M400 800 C520 790 620 830 760 860 C880 880 1000 800 1090 640 C1140 550 1175 420 1200 320 L1200 896 L400 896 Z" fill="var(--violet-wave)"/>
    <path d="M1060 640 C1120 560 1170 440 1200 390 L1200 896 L1000 896 C1060 820 1080 720 1060 640 Z" fill="var(--blue-wave)"/>
    <path d="M1110 520 C1140 460 1170 380 1200 350 L1200 420 C1170 460 1140 520 1110 560 Z" fill="var(--cyan-light)" opacity=".7"/>
    <path d="M845 470 C790 530 790 700 870 780" fill="none" stroke="var(--cyan)" stroke-width="10"/>
    <rect x="400" y="0" width="4" height="896" fill="#000" opacity=".05"/>
    <rect x="800" y="0" width="4" height="896" fill="#000" opacity=".07"/>
  </svg>

  <section class="panel panel-about">
    <div class="about-photo" role="img" aria-label="Photo of two healthcare professionals in white coats reviewing notes at a desk"></div>
    <div class="about-body">
      <h2 class="about-title">About Us</h2>
      <h3 class="about-sub">Our Mission</h3>
      <p class="about-text">Partner with clients to increase the value and security of their technology tools.</p>
      <h3 class="about-sub">Our Goal</h3>
      <p class="about-text">Become the premiere consulting company for Information Technology in the post-acute care industries.</p>
    </div>
  </section>

  <section class="panel panel-values">
    <div class="values-box">
      <h2 class="section-title">OUR <b>CORE VALUES</b></h2>
      <div class="value" style="left:0;top:80px;">
        <div class="value-tile"><svg width="40" height="40" viewBox="0 0 40 40"><circle cx="20" cy="20" r="17" fill="none" stroke="#fff" stroke-width="2"/><circle cx="20" cy="15" r="5" fill="#fff"/><path d="M10 28 Q20 18 30 28 Z" fill="#fff"/></svg></div>
        <div class="value-label">CLIENT FOCUSED</div>
      </div>
      <div class="value" style="left:118px;top:80px;">
        <div class="value-tile"><svg width="46" height="36" viewBox="0 0 46 36"><circle cx="9" cy="7" r="4" fill="#fff"/><circle cx="37" cy="7" r="4" fill="#fff"/><rect x="14" y="14" width="18" height="3" fill="#fff"/><rect x="21" y="17" width="3" height="16" fill="#fff"/><path d="M4 13h8v12H4zM34 13h8v12h-8z" fill="#fff"/></svg></div>
        <div class="value-label">ACCOUNTABILITY</div>
      </div>
      <div class="value" style="left:0;top:203px;">
        <div class="value-tile"><svg width="40" height="40" viewBox="0 0 40 40"><path d="M20 4 C11 4 7 12 9 20 L7 24 L10 25 L10 32 L18 32 L18 37 L30 37 L30 26 C34 22 34 4 20 4 Z" fill="#fff"/><path d="M14 18h14M21 14v12M16 18l-2 5h4zM28 18l-2 5h4z" stroke="var(--purple)" stroke-width="1.5" fill="none"/></svg></div>
        <div class="value-label big">INTEGRITY</div>
      </div>
      <div class="value" style="left:118px;top:203px;">
        <div class="value-tile"><svg width="40" height="36" viewBox="0 0 40 36"><circle cx="20" cy="5" r="3.5" fill="#fff"/><path d="M17 10h6l-2 9-4 5" stroke="#fff" stroke-width="3" fill="none"/><rect x="3" y="28" width="6" height="6" fill="#fff"/><rect x="12" y="24" width="6" height="10" fill="#fff"/><rect x="22" y="20" width="6" height="14" fill="#fff"/><rect x="31" y="16" width="6" height="18" fill="#fff"/></svg></div>
        <div class="value-label">PROFESSIONAL<br>DEVELOPMENT</div>
      </div>
    </div>

    <h2 class="section-title objective-title">OUR <b>PRIMARY OBJECTIVE</b></h2>
    <div class="objective" style="top:440px;">
      <svg width="50" height="46" viewBox="0 0 50 46" fill="none" stroke="var(--purple)" stroke-width="2.5"><circle cx="25" cy="12" r="5"/><path d="M16 30 Q25 16 34 30"/><path d="M4 23h8M46 23h-8M10 8l5 5M40 8l-5 5M10 38l5-5M40 38l-5-5M25 34v8"/></svg>
      <span>Understand and exceed<br>client expectations</span>
    </div>
    <div class="objective" style="top:510px;">
      <svg width="50" height="46" viewBox="0 0 50 46" fill="none" stroke="var(--purple)" stroke-width="2.5"><circle cx="12" cy="8" r="5"/><circle cx="38" cy="8" r="5"/><path d="M4 42V24q8-10 16 0v18M30 42V24q8-10 16 0v18M18 30h14"/></svg>
      <span>Committed to be a partner,<br>not vendor</span>
    </div>
    <div class="objective" style="top:575px;">
      <svg width="50" height="46" viewBox="0 0 50 46" fill="none" stroke="var(--purple)" stroke-width="2.5"><circle cx="25" cy="8" r="5"/><path d="M16 22q9-10 18 0"/><circle cx="9" cy="30" r="4"/><circle cx="41" cy="30" r="4"/><path d="M2 44q7-9 14 0M34 44q7-9 14 0M17 34h16"/></svg>
      <span>Provide simplified change<br>management expertise</span>
    </div>

    <div class="badge"><div class="badge-inner"><svg width="130" height="130" viewBox="0 0 130 130" aria-hidden="true"><circle cx="65" cy="65" r="60" fill="#3a3f5c"/></svg></div></div>
  </section>

  <section class="panel panel-services">
    <h2 class="section-title services-title">OUR <b>SERVICES</b></h2>
    <p class="services-text">We understand different organizations have different needs. Brevalink Pro strives to assist your organization by bringing solutions that are easy to understand and allow the client to track success. We provide solutions based on the client’s needs and desires.</p>
    <h3 class="it-title">Information Technology</h3>
    <ul class="it-list">
      <li><svg width="12" height="10" viewBox="0 0 12 10"><path d="M1 5l3.5 3.5L11 1" stroke="var(--purple)" stroke-width="2.4" fill="none"/></svg>CIO or IT Director Services</li>
      <li><svg width="12" height="10" viewBox="0 0 12 10"><path d="M1 5l3.5 3.5L11 1" stroke="var(--purple)" stroke-width="2.4" fill="none"/></svg>CISO or Information Security Officer</li>
      <li><svg width="12" height="10" viewBox="0 0 12 10"><path d="M1 5l3.5 3.5L11 1" stroke="var(--purple)" stroke-width="2.4" fill="none"/></svg>Comprehensive ePHI Risk Assessments</li>
      <li><svg width="12" height="10" viewBox="0 0 12 10"><path d="M1 5l3.5 3.5L11 1" stroke="var(--purple)" stroke-width="2.4" fill="none"/></svg>IT Department Evaluation</li>
      <li><svg width="12" height="10" viewBox="0 0 12 10"><path d="M1 5l3.5 3.5L11 1" stroke="var(--purple)" stroke-width="2.4" fill="none"/></svg>Policy Management and Consulting</li>
      <li><svg width="12" height="10" viewBox="0 0 12 10"><path d="M1 5l3.5 3.5L11 1" stroke="var(--purple)" stroke-width="2.4" fill="none"/></svg>On-going IT department support</li>
    </ul>
    <div class="it-photo" role="img" aria-label="Circular photo of a hand touching a glowing hexagon technology interface"></div>
  </section>
</main>
</body>
</html>
```